Willowmere Recovery Brochure

We need a brochure template we can change photo's and words at a later date. WE offer rehabilitation to injured horses and ponies.
Either use our Willowmere Grounds or Willowmere Recovery logo but not both. A strong preference for the horse being led to feature first.

Target Market(s)

Horse Owners

Font styles to use
Serif

Colors
f78f20

Requirements
Must have
• Ability to write the text and interchange photos within the layout at a later date.
Nice to have
• Our colours are orange and black

```html
<!DOCTYPE html>
<html lang="en">
<head>
<meta charset="utf-8">
<title>Willowmere Recovery Brochure</title>
<link href="https://fonts.googleapis.com/css2?family=Cinzel:wght@400;700&family=Arimo:wght@400&display=swap" rel="stylesheet">
<style>
  :root{
    --cream:#fbf4b9;
    --peach:#f8c98a;
    --orange:#f58a52;
    --brand-orange:#f07a2c;
    --red:#e5392a;
    --ink:#1f1410;
    --text:#1d1a17;
    --white:#ffffff;
  }
  html,body{margin:0;padding:0;overflow:hidden}
  body{width:1200px;height:849px}
  .brochure{
    position:relative;width:1200px;height:849px;overflow:hidden;
    background:linear-gradient(180deg,var(--cream) 0%,#fbe7a6 35%,var(--peach) 60%,var(--orange) 90%);
    font-family:"Arimo",Arial,sans-serif;color:var(--text);
  }
  .base-band{position:absolute;inset:0;width:1200px;height:849px}
  .panel-rule{position:absolute;top:0;width:1px;height:849px;background:rgba(60,40,20,.35)}
  .intro-box{position:absolute;left:400px;top:0;width:400px;height:482px;border-bottom:1px solid rgba(60,40,20,.3)}
  .brand{position:absolute;left:186px;top:52px;display:flex;align-items:center;gap:8px}
  .brand-name{font-family:"Cinzel",serif;font-size:17px;line-height:19px;color:var(--red);text-align:right;width:120px}
  .brand-mark{width:44px;height:72px;background:var(--brand-orange)}
  .section-title{position:absolute;font-family:"Cinzel",serif;color:var(--red);font-weight:400;margin:0}
  .about-title{left:48px;top:198px;font-size:30px;letter-spacing:1px}
  .body-copy{position:absolute;font-size:11.6px;line-height:15.6px;text-align:justify;margin:0}
  .body-copy p{margin:0 0 8.5px}
  .about-copy{left:48px;top:247px;width:306px}
  .banner{position:absolute;left:401px;top:65px;width:350px;height:54px;
    background:linear-gradient(90deg,var(--red) 0 262px,var(--brand-orange) 262px)}
  .banner h2{margin:0;font-family:"Cinzel",serif;font-weight:400;font-size:37px;color:var(--white);line-height:54px;padding-left:22px;letter-spacing:1px}
  .rehab-copy{left:437px;top:135px;width:318px}
  .rehab-copy p{margin:0}
  .listing{position:absolute;left:438px;top:330px;width:330px;font-family:"Cinzel",serif;font-size:23px;line-height:24px;color:#3a2a20;margin:0;letter-spacing:.5px}
  .listing .big{font-size:26px}
  .listing .invite{display:block;color:var(--red);margin-top:4px;line-height:23px}
  .photo{position:absolute}
  .photo-cookie{left:401px;top:482px;width:399px;height:272px;clip-path:polygon(0 0,100% 0,100% 248px,0 272px);
    background:linear-gradient(160deg,#4a5a2c 0%,#7e8f4a 40%,#c9bfa0 65%,#6b7a3a 100%)}
  .photo-title{position:absolute;left:424px;top:498px;font-family:"Cinzel",serif;font-weight:700;font-size:20px;color:var(--white);margin:0;text-shadow:0 1px 3px rgba(0,0,0,.6)}
  .caption-orange{position:absolute;left:432px;top:765px;width:330px;font-size:14px;line-height:19px;color:var(--brand-orange);margin:0}
  .horse-head{position:absolute;font-family:"Cinzel",serif;font-weight:400;color:#1f1712;margin:0;right:54px;font-size:21px;letter-spacing:.5px}
  .horse-head small{font-size:16px}
  .head-lady{top:60px}
  .head-charlotte{top:370px}
  .photo-lady{left:800px;top:98px;width:347px;height:205px;background:linear-gradient(180deg,#a9b9a2 0%,#8aa06a 45%,#6e8f3a 100%)}
  .photo-charlotte{left:800px;top:403px;width:347px;height:205px;background:linear-gradient(90deg,#2a2420 0%,#7b4a2a 35%,#9c8f7e 60%,#6a3a22 100%)}
  .caption-right{position:absolute;right:63px;top:312px;font-size:14px;margin:0}
  .charlotte-copy{left:843px;top:620px;width:304px;font-size:11.6px}
  .web{position:absolute;right:34px;top:804px;color:var(--white);font-size:14px;margin:0}
</style>
</head>
<body>
<div class="brochure">
  <svg class="base-band" viewBox="0 0 1200 849" aria-hidden="true">
    <polygon points="0,777 1200,706 1200,849 0,849" fill="#1f1410"/>
  </svg>
  <div class="intro-box"></div>
  <div class="panel-rule" style="left:400px"></div>
  <div class="panel-rule" style="left:800px"></div>

  <!-- Left panel -->
  <div class="brand">
    <div class="brand-name">Willowmere Recovery</div>
    <div class="brand-mark"></div>
  </div>
  <h1 class="section-title about-title">Willowmere</h1>
  <div class="body-copy about-copy">
    <p>Willowmere Equine Sanctuary (WES) was founded by passionate animal lovers and advocates in 2014, in response to an ever-increasing number of horses passing through the saleyards, and into the hands of knackeries.</p>
    <p>The name was selected to pay homage to the brilliant protective work done by the Ocean Keepers, and to reflect our mission of providing sanctuary and solace to unwanted, injured, and otherwise vulnerable horses and ponies. We are a fully NCRA registered charity, and rely largely on funding from committee members, and a small number of sponsors, to continue our work.</p>
    <p>Last year (2016) has been one of tremendous growth for WES, commencing with the move to our new, 200 acre Sanctuary in Ashby, Victoria. This was promptly followed by the arrival of 113 horses as part of the largest AWSA horse seizure in Australian history.</p>
    <p>Then, in April, WES was again selected by the AWSA to care for the tragic Riverbend horses; horses that had suffered the most horrific neglect, and generated unprecedented public outrage.</p>
    <p>Today, WES is currently home to over 150 horses and ponies, along with many other rescue animals, including dogs, cats, donkeys, goats, sheep, cows, ex-battery hens, geese, ducks, alpacas… Even turkeys!</p>
  </div>

  <!-- Middle panel -->
  <div class="banner"><h2>Rehabilitation</h2></div>
  <div class="body-copy rehab-copy">
    <p>Horses that first come to the Sanctuary are given time to unwind, relax and in turn, be assessed for rehabilitation needs.</p>
    <p>Each horse will always have its own specific needs addressed and for us, there is no rush. Taking time to learn more about each horse allows us to better assess them for adoption suitability. We take the worry out of purchasing an ‘unknown’ horse for you.</p>
    <p>Your ongoing support of donations enables us to continue saving and rehabilitating horses giving them a second chance in life.</p>
  </div>
  <p class="listing"><span class="big">L</span>isted below<br>are our current horses<br>under rehabilitation –<span class="invite">we welcome expressions<br>of interest:</span></p>
  <div class="photo photo-cookie" role="img" aria-label="Photo: handler leading a small chestnut pony along a tree-lined farm track with a dog"></div>
  <h3 class="photo-title">WES COOKIE IN TRAINING</h3>
  <p class="caption-orange">Beautiful little Cookie is only 11hh high and would make a super companion pony.</p>

  <!-- Right panel -->
  <h3 class="horse-head head-lady">WES LADY – FOR ADOPTION</h3>
  <div class="photo photo-lady" role="img" aria-label="Photo: bay mare grazing in a green paddock beside her foal"></div>
  <p class="caption-right">WES Lady times 2</p>
  <h3 class="horse-head head-charlotte">WES CHARLOTTE – <small>COMPANION</small></h3>
  <div class="photo photo-charlotte" role="img" aria-label="Photos: chestnut mare looking out of a stable door, and standing rugged in a barn"></div>
  <p class="body-copy charlotte-copy">Beautiful older companion mare – has had a rough few years and now needs someone kind to help her retire gracefully.</p>
  <p class="web">www.willowmere.org.au</p>
</div>
</body>
</html>
```